Brightwell Consulting Business Card Design

Business Card Design for Brightwell Consulting. Brightwell Consulting is a boutique consultancy based in Atlanta, GA., that specializes in marketing strategy, organization planning, and leadership development. We provide solutions for small businesses and startups as well as Summit 400 companies.

http://brightwellconsulting.example/

Target Market(s)

We provide solutions for small businesses and startups as well as Summit 400 companies.

Industry/Entity Type

Consulting

Contact Information for Business Card

Two sided business card with priority on contact information, logo, tag line (Guidance to aim higher, reach further, grow stronger)

Colors

Designer to choose colors to be used in the design.

Requirements
Must have
• contact information, logo, tag line (Guidance to aim higher, reach further, grow stronger)
• Simple no over communication.
Nice to have
• I would like to see different placements of logo and creative use of both sides of the card
Should not have
• Do not put too much information on the card.

```html
<!DOCTYPE html>
<html lang="en">
<head>
<meta charset="utf-8">
<title>Brightwell Consulting – Business Card</title>
<link rel="stylesheet" href="https://fonts.googleapis.com/css2?family=Open+Sans:wght@400;600;700&display=swap">
<style>
  :root {
    --page: #e9e6e1;
    --card: #050505;
    --card-band: #151617;
    --rule: #f2f2f2;
    --text: #ffffff;
    --text-soft: #d4d4d4;
    --pattern-a: #3a3b3d;
  }
  * { box-sizing: border-box; margin: 0; padding: 0; }
  html, body {
    width: 1200px; height: 900px; overflow: hidden;
    background: var(--page);
    font-family: "Open Sans", Arial, sans-serif;
  }
  .canvas { position: relative; width: 1200px; height: 900px; }
  .card {
    position: absolute; width: 700px; height: 400px;
    background: var(--card); overflow: hidden;
    box-shadow: 0 12px 30px rgba(0,0,0,0.25);
    color: var(--text);
  }
  .card--back { left: 80px; top: 40px; }
  .card--front { left: 420px; top: 470px; }

  .wordmark {
    font-family: "Open Sans", Arial, sans-serif;
    font-weight: 700; color: var(--text); white-space: nowrap;
  }

  /* contact side */
  .rule { position: absolute; left: 0; width: 100%; height: 3px; background: var(--rule); }
  .rule--upper { top: 185px; }
  .rule--lower { top: 292px; }
  .contact-band {
    position: absolute; left: 0; top: 295px; width: 100%; height: 105px;
    background: var(--card-band);
  }
  .band-texture {
    position: absolute; right: 0; top: 188px; width: 380px; height: 212px;
    background: radial-gradient(ellipse at 100% 0%, var(--pattern-a) 0%, rgba(30,30,32,0.6) 40%, rgba(10,10,10,0) 75%);
  }
  .card--back .wordmark { position: absolute; left: 56px; top: 204px; font-size: 30px; }
  .tagline {
    position: absolute; left: 56px; top: 252px;
    font-size: 17px; font-weight: 600; color: var(--text); white-space: nowrap;
  }
  .contact-list {
    position: absolute; left: 56px; top: 306px; list-style: none;
  }
  .contact-list li {
    display: flex; align-items: center; gap: 14px;
    height: 28px; font-size: 14px; letter-spacing: 1.5px;
    text-transform: uppercase; color: var(--text-soft); white-space: nowrap;
  }
  .contact-list svg { width: 18px; height: 18px; fill: none; stroke: var(--text); stroke-width: 1.6; flex: none; }
  .contact-list .icon-solid { fill: var(--text); stroke: none; }

  /* logo side */
  .front-texture {
    position: absolute; right: 0; top: 0; width: 420px; height: 400px;
    background: radial-gradient(ellipse at 100% 10%, var(--pattern-a) 0%, rgba(28,28,30,0.7) 35%, rgba(5,5,5,0) 70%);
  }
  .card--front .wordmark {
    position: absolute; left: 130px; top: 170px; font-size: 40px;
  }
</style>
</head>
<body>
<main class="canvas">

  <section class="card card--back" aria-label="Contact side of the business card">
    <div class="band-texture" role="img" aria-label="Soft grey layered wave pattern"></div>
    <div class="rule rule--upper"></div>
    <p class="wordmark">Brightwell Consulting</p>
    <p class="tagline">Guidance to aim higher, reach further, grow stronger</p>
    <div class="rule rule--lower"></div>
    <div class="contact-band"></div>
    <ul class="contact-list">
      <li>
        <svg viewBox="0 0 20 20" aria-hidden="true"><rect x="2" y="5" width="16" height="11" class="icon-solid"/><path d="M2 5 L10 11 L18 5" stroke="#050505" stroke-width="1.4" fill="none"/></svg>
        jordan@brightwellconsulting.example
      </li>
      <li>
        <svg viewBox="0 0 20 20" aria-hidden="true"><path class="icon-solid" d="M5 2 L8 2 L9 6 L7 8 Q9 12 12 13 L14 11 L18 12 L18 15 Q17 18 14 18 Q4 16 2 6 Q2 3 5 2 Z"/></svg>
        555-013-2468
      </li>
      <li>
        <svg viewBox="0 0 20 20" aria-hidden="true"><circle cx="10" cy="10" r="8"/><ellipse cx="10" cy="10" rx="3.5" ry="8"/><path d="M2 10 H18 M3.5 6 H16.5 M3.5 14 H16.5"/></svg>
        http://brightwellconsulting.example/home.html
      </li>
    </ul>
  </section>

  <section class="card card--front" aria-label="Logo side of the business card">
    <div class="front-texture" role="img" aria-label="Soft grey layered wave pattern in the corner"></div>
    <p class="wordmark">Brightwell Consulting</p>
  </section>

</main>
</body>
</html>
```